Landscape Contractor in need of New Web Design

HELP.. Please Help!!!!. Our current website is old, outdated, ugly... and well nothing like us.... so we are looking for someone to help build a new website that fits our company direction. We are a landscape company with multiple locations in order to meet the needs of our clients and their projects throughout the midwest. When most people think of landscaping, they think of mowing grandmas yard, but that is NOT even remotely close to what we do. We are 100% a commercial landscape company meaning we complete landscape and irrigation services for large scale commercial projects. We are looking for a website to showcase our commercial talents and awesome team of people.
Updates

Address of current website is www.brookvaleyardworks.com

```html
<!DOCTYPE html>
<html lang="en">
<head>
<meta charset="utf-8">
<title>Brookvale Yardworks — Landscape and Irrigation</title>
<link href="https://fonts.googleapis.com/css2?family=Montserrat:wght@500;600;700;800&family=Nunito+Sans:wght@400;600;700&display=swap" rel="stylesheet">
<style>
:root{
  --green:#8fef00;
  --green-dark:#6cc400;
  --ink:#1b1b1b;
  --text:#3a3a3a;
  --muted:#5a5a5a;
  --light:#f1f0f2;
  --dark:#1d1d1d;
  --field:#2a2a2a;
  --white:#ffffff;
}
*{box-sizing:border-box;margin:0;padding:0}
html,body{width:1200px;height:4127px;overflow:hidden}
body{position:relative;font-family:"Nunito Sans",Arial,sans-serif;color:var(--text);background:var(--white)}

/* header */
.site-header{position:absolute;left:0;top:0;width:1200px;height:125px;background:var(--white)}
.brand{position:absolute;left:131px;top:22px;display:flex;align-items:center;gap:10px}
.brand-dot{width:18px;height:18px;border-radius:50%;background:var(--green)}
.brand-name{font-family:"Montserrat",sans-serif;font-weight:700;font-size:20px;color:var(--ink);line-height:1.1}
.call{position:absolute;left:628px;top:26px;display:flex;align-items:center;gap:12px}
.round-icon{width:30px;height:30px;border-radius:50%;background:var(--green);display:flex;align-items:center;justify-content:center}
.call-label{font-size:12px;color:var(--ink);letter-spacing:.5px}
.call-nums{font-size:15px;font-weight:700;color:var(--ink)}
.btn{display:flex;align-items:center;justify-content:center;background:var(--green);color:var(--ink);font-family:"Montserrat",sans-serif;font-weight:700;border-radius:8px}
.btn-top{position:absolute;left:929px;top:26px;width:138px;height:35px;font-size:13px}
.nav{position:absolute;top:88px;left:0;width:1200px;font-family:"Montserrat",sans-serif;font-size:14px;font-weight:500;color:var(--ink);letter-spacing:.5px}
.nav span{position:absolute}
.nav .active::after{content:"";position:absolute;left:0;right:0;bottom:-9px;height:2px;background:var(--green)}

/* hero */
.hero{position:absolute;left:0;top:125px;width:1200px;height:593px;background:linear-gradient(115deg,#5c4a36 0%,#8f8577 22%,#b9a79a 45%,#6f8f3a 70%,#3f6b1e 100%)}
.hero-shade{position:absolute;inset:0;background:linear-gradient(90deg,rgba(0,0,0,.45),rgba(0,0,0,0) 60%)}
.hero-title{position:absolute;left:133px;top:292px;font-family:"Montserrat",sans-serif;font-weight:800;font-size:47px;line-height:57px;color:var(--white)}
.hero-sub{position:absolute;left:133px;top:424px;width:400px;font-family:"Montserrat",sans-serif;font-weight:700;font-size:18px;line-height:25px;color:var(--white)}
.btn-hero{position:absolute;left:133px;top:504px;width:194px;height:52px;font-size:19px;border-radius:10px}
.dots{position:absolute;left:560px;display:flex;gap:9px;align-items:center}
.dots i{width:6px;height:6px;border-radius:50%;background:rgba(255,255,255,.8)}
.dots i.on{width:10px;height:10px;background:#f08a1a}

/* section titles */
.sec-title{position:absolute;left:0;width:1200px;text-align:center;font-family:"Montserrat",sans-serif;font-weight:700;font-size:25px;color:var(--ink)}
.sec-rule{position:absolute;left:585px;width:30px;height:4px;background:var(--green);border-radius:2px}

/* photo cards */
.card{position:absolute;border-radius:8px;overflow:hidden;box-shadow:0 3px 8px rgba(0,0,0,.18)}
.card-fade{position:absolute;left:0;right:0;bottom:0;height:45%;background:linear-gradient(transparent,rgba(0,0,0,.75))}
.card-label{position:absolute;left:14px;bottom:14px;font-family:"Montserrat",sans-serif;font-weight:700;font-size:14px;line-height:18px;color:var(--white);letter-spacing:.3px}
.card-label::before{content:"";position:absolute;left:0;top:-12px;width:114px;height:2px;background:var(--green)}

/* why */
.why{position:absolute;left:0;top:1378px;width:1200px;height:554px;background:var(--light)}
.why-icon{position:absolute;width:70px;height:70px;border-radius:50%;background:var(--green);display:flex;align-items:center;justify-content:center}
.why-text{position:absolute;width:190px}
.why-text h4{font-family:"Montserrat",sans-serif;font-weight:700;font-size:13px;color:var(--ink);margin-bottom:8px}
.why-text p{font-size:12px;line-height:16px;color:var(--muted)}
.why-photo{position:absolute;left:413px;top:1517px;width:375px;height:239px;border-radius:18px;background:linear-gradient(135deg,#3f6a22 0%,#c9a97c 50%,#5b8a2e 100%);box-shadow:0 4px 12px rgba(0,0,0,.18)}

/* we are */
.intro{position:absolute;left:0;top:2030px;width:1200px;text-align:center;font-size:16px;line-height:24px;color:var(--text)}

/* testimonials */
.testi{position:absolute;left:0;top:2683px;width:1200px;height:542px;background:linear-gradient(100deg,#5f7f2e 0%,#8aa86a 35%,#6f6252 60%,#7d9150 100%)}
.testi-title{position:absolute;left:0;top:2733px;width:1200px;text-align:center;font-family:"Montserrat",sans-serif;font-weight:700;font-size:25px;color:var(--white)}
.t-card{position:absolute;top:2821px;width:300px;height:343px;background:var(--white);border-radius:6px;text-align:center;padding:30px 32px 0}
.t-quote{font-family:Georgia,serif;font-size:40px;line-height:30px;color:var(--ink);font-style:italic;height:38px}
.t-body{font-size:13px;line-height:20px;color:var(--text);height:200px}
.t-more{font-size:11px;font-weight:700;text-decoration:underline;color:var(--ink)}
.t-rule{width:40px;height:2px;background:var(--green);margin:0 auto 18px}
.t-name{font-family:"Montserrat",sans-serif;font-weight:700;font-size:13px;color:var(--ink)}
.t-co{font-size:11.5px;color:var(--muted);margin-top:3px}
.arrow{position:absolute;top:2974px}

/* quote form */
.quote{position:absolute;left:0;top:3225px;width:1200px;height:548px;background:var(--dark)}
.quote-title{position:absolute;left:0;top:3272px;width:1200px;text-align:center;font-family:"Montserrat",sans-serif;font-weight:700;font-size:25px;color:var(--white)}
.field{position:absolute;background:var(--field);border:1px solid #3e3e3e;border-radius:6px;color:#c9c9c9;font-size:12px;padding:0 22px;display:flex;align-items:center}
.field.area{align-items:flex-start;padding-top:16px}
.btn-submit{position:absolute;left:535px;top:3664px;width:130px;height:51px;font-size:19px;border-radius:10px}

/* footer */
.footer{position:absolute;left:0;top:3773px;width:1200px;height:354px;background:var(--white)}
.foot-brand{position:absolute;left:149px;top:3860px;display:flex;align-items:center;gap:12px}
.foot-brand .brand-dot{width:26px;height:26px}
.foot-brand .brand-name{font-size:24px}
.foot-h{position:absolute;top:3820px;font-family:"Montserrat",sans-serif;font-weight:700;font-size:13px;color:var(--ink)}
.foot-menu{position:absolute;left:434px;top:3855px;font-size:12px;line-height:19px;color:var(--text);letter-spacing:.3px}
.foot-row{position:absolute;display:flex;align-items:flex-start;gap:12px;font-size:12px;line-height:16px;color:var(--text)}
.foot-row .ic{width:22px;height:22px;border-radius:50%;flex:none;display:flex;align-items:center;justify-content:center;margin-top:2px}
.ic.g{background:var(--green)}
.ic.d{background:var(--ink)}
.copy{position:absolute;left:0;top:4075px;width:1200px;text-align:center;font-size:12px;color:var(--text)}
</style>
</head>
<body>

<header class="site-header">
  <div class="brand"><span class="brand-dot"></span><span class="brand-name">Brookvale<br>Yardworks</span></div>
  <div class="call">
    <span class="round-icon"><svg width="14" height="14" viewBox="0 0 24 24"><path d="M6.6 10.8a15 15 0 0 0 6.6 6.6l2.2-2.2c.3-.3.7-.4 1-.2 1.1.4 2.3.6 3.6.6.6 0 1 .4 1 1V20c0 .6-.4 1-1 1A17 17 0 0 1 3 4c0-.6.4-1 1-1h3.5c.6 0 1 .4 1 1 0 1.2.2 2.4.6 3.6.1.3 0 .7-.2 1z" fill="#1b1b1b"/></svg></span>
    <div><div class="call-label">CALL US</div><div class="call-nums">(555) 318-2047 &nbsp;|&nbsp; (555) 604-7712</div></div>
  </div>
  <div class="btn btn-top">GET A QUOTE</div>
  <nav class="nav">
    <span class="active" style="left:434px">HOME</span>
    <span style="left:519px">DIVISIONS</span>
    <span style="left:642px">SERVICES</span>
    <span style="left:761px">ABOUT US</span>
    <span style="left:886px">GALLERY</span>
    <span style="left:996px">CONTACT</span>
  </nav>
</header>

<section class="hero" role="img" aria-label="Worker kneeling to lay a roll of fresh sod beside a paver walkway and gravel bed">
  <div class="hero-shade"></div>
</section>
<h1 class="hero-title">TURF<br>INSTALLATION</h1>
<p class="hero-sub">Lorem Ipsum is simply dummy text of the printing and typesetting industry</p>
<div class="btn btn-hero">GET A QUOTE</div>
<div class="dots" style="top:673px"><i></i><i></i><i class="on"></i><i></i><i></i></div>

<!-- services -->
<h2 class="sec-title" style="top:762px">OUR SERVICES</h2>
<div class="sec-rule" style="top:805px"></div>

<div class="card" style="left:131px;top:846px;width:298px;height:224px;background:linear-gradient(160deg,#3f7a1e,#6aa32f 55%,#2f5d16)" role="img" aria-label="Ride-on mower cutting striped lawn"><div class="card-fade"></div><div class="card-label">MAINTENANCE</div></div>
<div class="card" style="left:450px;top:846px;width:298px;height:224px;background:linear-gradient(160deg,#d9e4a8,#7fae3a 45%,#3d6a1f)" role="img" aria-label="Sprinklers watering a sunlit park lawn"><div class="card-fade"></div><div class="card-label">TURF MANAGEMENT</div></div>
<div class="card" style="left:769px;top:846px;width:298px;height:224px;background:linear-gradient(160deg,#5e7d3e,#9e9a92 50%,#6f6a63)" role="img" aria-label="Stone retaining wall and steps"><div class="card-fade"></div><div class="card-label">HARDSCAPING</div></div>
<div class="card" style="left:131px;top:1093px;width:298px;height:224px;background:linear-gradient(160deg,#e8f0b0,#9fcf4a 45%,#4e8a22)" role="img" aria-label="Pop-up sprinkler spraying water across grass"><div class="card-fade"></div><div class="card-label">IRRIGATION</div></div>
<div class="card" style="left:450px;top:1093px;width:298px;height:224px;background:linear-gradient(160deg,#6a3a5e,#7fa83a 40%,#8d8a80 65%,#b23a4a)" role="img" aria-label="Curving paver path through flower beds and hedges"><div class="card-fade"></div><div class="card-label">LANDSCAPING</div></div>
<div class="card" style="left:769px;top:1093px;width:298px;height:224px;background:linear-gradient(160deg,#c8ccc9,#8e8676 45%,#4f7a2e)" role="img" aria-label="Large stone house with a well-kept front lawn"><div class="card-fade"></div><div class="card-label">CHEMICAL APPLICATIONS<br>&amp; FERTILIZATION</div></div>

<!-- why choose us -->
<section class="why"></section>
<h2 class="sec-title" style="top:1422px">WHY CHOOSE US?</h2>
<div class="sec-rule" style="top:1465px"></div>

<div class="why-photo" role="img" aria-label="Curved stone garden border with flowering plants"></div>

<div class="why-icon" style="left:122px;top:1511px"><svg width="38" height="30" viewBox="0 0 38 30"><path d="M2 28 L6 12 L9 22 L12 6 L15 20 L19 2 L23 20 L26 6 L29 22 L32 12 L36 28 Z" fill="#1b1b1b"/></svg></div>
<div class="why-text" style="left:211px;top:1506px"><h4>Specialized Company</h4><p>Brookvale Yardworks strives to set the standard for the highest quality lawn and landscape products and services and to exceed our customer's expectations every time.</p></div>

<div class="why-icon" style="left:122px;top:1673px"><svg width="34" height="30" viewBox="0 0 34 30" fill="none" stroke="#1b1b1b" stroke-width="2"><rect x="2" y="3" width="26" height="20" rx="2"/><path d="M7 9h16M7 14h10"/><circle cx="26" cy="21" r="5" fill="#8fef00"/><path d="M23 25l-1 4 4-2 4 2-1-4"/></svg></div>
<div class="why-text" style="left:207px;top:1670px"><h4>Licensed &amp; Insured</h4><p>Rest assured knowing that Brookvale Yardworks, Inc. is fully licensed and insured and has a superior safety rating.</p></div>

<div class="why-icon" style="left:266px;top:1800px"><svg width="34" height="30" viewBox="0 0 34 30" fill="none" stroke="#1b1b1b" stroke-width="2.2"><path d="M4 3h26v18H13l-7 6v-6H4z"/><path d="M10 10h14M10 15h10"/></svg></div>
<div class="why-text" style="left:357px;top:1796px;width:240px"><h4>Dependable Services</h4><p>Communication is highly valued at Brookvale Yardworks. From start to finish our clients will be kept up to date on their project.</p></div>

<div class="why-icon" style="left:806px;top:1508px"><svg width="34" height="28" viewBox="0 0 34 28"><rect x="2" y="7" width="30" height="19" rx="2" fill="#1b1b1b"/><path d="M12 7V3h10v4" fill="none" stroke="#1b1b1b" stroke-width="2.5"/><rect x="14" y="13" width="6" height="4" fill="#8fef00"/></svg></div>
<div class="why-text" style="left:893px;top:1506px;width:205px"><h4>Reputable Company</h4><p>With 15 years of experience in the landscaping construction business, we have built a reputation for superior projects and service.</p></div>

<div class="why-icon" style="left:811px;top:1642px"><svg width="32" height="32" viewBox="0 0 24 24" fill="none" stroke="#1b1b1b" stroke-width="1.8"><path d="M6.6 10.8a15 15 0 0 0 6.6 6.6l2.2-2.2c.3-.3.7-.4 1-.2 1.1.4 2.3.6 3.6.6.6 0 1 .4 1 1V20c0 .6-.4 1-1 1A17 17 0 0 1 3 4c0-.6.4-1 1-1h3.5c.6 0 1 .4 1 1 0 1.2.2 2.4.6 3.6.1.3 0 .7-.2 1z"/><path d="M14 3a7 7 0 0 1 7 7M14 6.5a3.5 3.5 0 0 1 3.5 3.5"/></svg></div>
<div class="why-text" style="left:901px;top:1641px;width:180px"><h4>Free Consultations</h4><p>Call our office to set up a time to meet with one of our qualified professionals. They will walk your property with you to help trouble shoot problems and work to bring your vision to life.</p></div>

<div class="why-icon" style="left:658px;top:1811px"><svg width="30" height="30" viewBox="0 0 30 30" fill="none" stroke="#1b1b1b" stroke-width="2.2"><rect x="3" y="5" width="24" height="22" rx="2"/><path d="M3 11h24M9 2v6M21 2v6"/><path d="M8 16h3M14 16h3M20 16h2M8 21h3M14 21h3M20 21h2" stroke-width="2.6"/></svg></div>
<div class="why-text" style="left:752px;top:1810px;width:250px"><h4>Day Scheduling</h4><p>Contact our office today to schedule an appointment that meets your needs!</p></div>

<!-- we are -->
<h2 class="sec-title" style="top:1985px">WE ARE</h2>
<p class="intro">Brookvale Yardworks, Inc. is a full service lawn and landscape contractor<br>providing design, installation, and maintenance services.</p>
<div class="sec-rule" style="top:2098px"></div>

<div class="card" style="left:131px;top:2150px;width:299px;height:226px;background:linear-gradient(160deg,#4a5a3a,#9a8a74 45%,#5d6e3a)" role="img" aria-label="Landscaped bed beside a retail fuel station"><div class="card-fade"></div><div class="card-label" style="left:22px">COMMERCIAL</div></div>
<div class="card" style="left:450px;top:2150px;width:299px;height:226px;background:linear-gradient(160deg,#c9c6c2,#8d857a 45%,#55802e)" role="img" aria-label="Government building entrance with flower beds"><div class="card-fade"></div><div class="card-label" style="left:22px">GOVERNMENT</div></div>
<div class="card" style="left:769px;top:2150px;width:299px;height:226px;background:linear-gradient(160deg,#b7b5a8,#6d8a3e 50%,#3d3a32)" role="img" aria-label="Residential front yard with walkway and planting beds"><div class="card-fade"></div><div class="card-label" style="left:22px">RESIDENTIAL</div></div>
<div class="card" style="left:131px;top:2395px;width:459px;height:226px;background:linear-gradient(160deg,#4a6a2a,#8a8f8a 50%,#3c4e2a)" role="img" aria-label="Rock waterfall feature surrounded by trees"><div class="card-fade"></div><div class="card-label" style="left:22px">MUNICIPALITY</div></div>
<div class="card" style="left:609px;top:2395px;width:458px;height:226px;background:linear-gradient(170deg,#2f5a46,#7a9a4a 45%,#9a7a56)" role="img" aria-label="Crew installing turf on a stadium field"><div class="card-fade"></div><div class="card-label" style="left:22px">COMMERCIAL</div></div>

<!-- testimonials -->
<section class="testi" role="img" aria-label="Worker laying rolls of sod on a lawn"></section>
<h2 class="testi-title">TESTIMONIALS</h2>
<div class="sec-rule" style="top:2782px"></div>

<svg class="arrow" style="left:70px" width="20" height="30" viewBox="0 0 20 30"><path d="M15 3L4 15l11 12" fill="none" stroke="#fff" stroke-width="3"/></svg>
<svg class="arrow" style="left:1108px" width="20" height="30" viewBox="0 0 20 30"><path d="M5 3l11 12L5 27" fill="none" stroke="#fff" stroke-width="3"/></svg>

<article class="t-card" style="left:131px">
  <div class="t-quote">&ldquo;</div>
  <p class="t-body">I have been working with Brookvale Yardworks for several years. As a building / development firm I understand the importance of landscaping in our projects. Brookvale Yardworks has provided expert landscape consultation and performance on all projects I have had the opportunity to work with them on.</p>
  <div class="t-rule"></div>
  <div class="t-name">DANIEL R HOLLIS</div>
  <div class="t-co">Hollis Building Group</div>
</article>
<article class="t-card" style="left:450px">
  <div class="t-quote">&ldquo;</div>
  <p class="t-body">As part of the Willow Ridge Development Company, I have been extremely pleased with the dramatic improvements to the landscape within the community evident since the beginning of Brookvale Yardworks's services. This opinion is shared by many of Willow Ridge's residents. We appreciate your skilled,<br><span class="t-more">MORE</span></p>
  <div class="t-rule"></div>
  <div class="t-name">DANIEL R HOLLIS</div>
  <div class="t-co">Hollis Building Group</div>
</article>
<article class="t-card" style="left:769px">
  <div class="t-quote">&ldquo;</div>
  <p class="t-body">I am writing this letter of recommendation for Brookvale Yardworks and Landscape... They manage their projects and crews in a professional and timely manner. Projects are on time and within budget despite the multitude of changes that are a part of everyday business in federal contracting.</p>
  <div class="t-rule"></div>
  <div class="t-name">DANIEL R HOLLIS</div>
  <div class="t-co">Hollis Building Group</div>
</article>

<!-- quote -->
<section class="quote"></section>
<h2 class="quote-title">REQUEST A QUICK QUOTE</h2>
<div class="sec-rule" style="top:3324px"></div>
<div class="field" style="left:276px;top:3379px;width:312px;height:46px">Your Name</div>
<div class="field" style="left:604px;top:3379px;width:312px;height:46px">Your Email</div>
<div class="field" style="left:276px;top:3446px;width:312px;height:48px;justify-content:space-between">Snow Removal<svg width="12" height="8" viewBox="0 0 12 8"><path d="M0 0h12L6 8z" fill="#fff"/></svg></div>
<div class="field" style="left:604px;top:3446px;width:312px;height:48px">Phone</div>
<div class="field area" style="left:276px;top:3515px;width:640px;height:117px">Message</div>
<div class="btn btn-submit">SUBMIT</div>

<!-- footer -->
<footer class="footer"></footer>
<div class="foot-brand"><span class="brand-dot"></span><span class="brand-name">Brookvale<br>Yardworks</span></div>

<div class="foot-h" style="left:434px">MENU</div>
<div class="foot-menu">ABOUT US<br>DIVISIONS<br>CERTIFICATIONS<br>GALLERY</div>

<div class="foot-h" style="left:657px">CONTACT US</div>
<div class="foot-row" style="left:657px;top:3856px"><span class="ic g"><svg width="10" height="12" viewBox="0 0 10 12"><path d="M5 0a4 4 0 0 1 4 4c0 3-4 8-4 8S1 7 1 4a4 4 0 0 1 4-4z" fill="#1b1b1b"/></svg></span><span>4180 W Meadowrun Lane<br>Millbrook, KS 66000</span></div>
<div class="foot-row" style="left:657px;top:3908px"><span class="ic g"><svg width="11" height="11" viewBox="0 0 24 24"><path d="M6.6 10.8a15 15 0 0 0 6.6 6.6l2.2-2.2c.3-.3.7-.4 1-.2 1.1.4 2.3.6 3.6.6.6 0 1 .4 1 1V20c0 .6-.4 1-1 1A17 17 0 0 1 3 4c0-.6.4-1 1-1h3.5c.6 0 1 .4 1 1 0 1.2.2 2.4.6 3.6.1.3 0 .7-.2 1z" fill="#1b1b1b"/></svg></span><span>Call Us<br>1-555-318-2047</span></div>
<div class="foot-row" style="left:657px;top:3960px"><span class="ic g"><svg width="11" height="9" viewBox="0 0 11 9"><rect x=".5" y=".5" width="10" height="8" fill="none" stroke="#1b1b1b"/><path d="M.5.5l5 4 5-4" fill="none" stroke="#1b1b1b"/></svg></span><span>E mail Us<br>office@brookvaleyardworks.com</span></div>

<div class="foot-h" style="left:961px">FOLLOW US</div>
<div class="foot-row" style="left:961px;top:3856px"><span class="ic d"></span><span>Like us on<br>GREENPOST</span></div>
<div class="foot-row" style="left:961px;top:3908px"><span class="ic d"></span><span>Follow us on<br>CHIRPER</span></div>
<div class="foot-row" style="left:961px;top:3960px"><span class="ic d"></span><span>Follow us on<br>WORKLINK</span></div>

<p class="copy">Copyright © 2021 All Rights Reserved</p>

</body>
</html>
```